Real Estate Wordpress Landing Page

I'm looking to a landing page dedicated to my real estate brokerage that's catered to promoting that my company provides 1.5% listings to home sellers... I have a couple examples that I'm really looking towards mocking in a version with similar color schemes using my current company colors/website.

http://lorvanta.com/
https://www.bluthorn.com/about/one-percent-listing-fee

My brokerage company website is http://www.calmridge.us/

Target Market(s)

real estate home sellers & buyers

Industry/Entity Type

Real Estate

Coding

Coded - Design and coding required

Number of Pages Required

1 page

Colors
3176b5
0255a3
eaf1f7
cedeed

Requirements
Must have
• Company website colors - http://www.calmridge.us/
• Something around the lines of this website page - http://lorvanta.com/
• Wordpress compatibility

```html
<!DOCTYPE html>
<html lang="en">
<head>
<meta charset="utf-8">
<title>Calmridge Realty – List for 1.5% Commission</title>
<link href="https://fonts.googleapis.com/css2?family=Oswald:wght@400;500;600&family=Titillium+Web:wght@400;600&display=swap" rel="stylesheet">
<style>
:root{
  --blue:#0255a3;
  --blue-mid:#3176b5;
  --blue-pale:#eaf1f7;
  --blue-soft:#cedeed;
  --red:#ee2a24;
  --ink:#1e1e1e;
  --muted:#555;
  --white:#fff;
}
*{box-sizing:border-box;margin:0;padding:0}
html,body{width:1200px;height:3114px;overflow:hidden;background:var(--white)}
body{position:relative;font-family:'Titillium Web',sans-serif;color:var(--ink)}
.abs{position:absolute}
.display{font-family:'Oswald',sans-serif;text-transform:uppercase}
.btn{position:absolute;background:var(--red);color:var(--white);font-family:'Oswald',sans-serif;font-weight:500;font-size:17px;letter-spacing:1.5px;text-transform:uppercase;display:flex;align-items:center;justify-content:center}
.phone{display:flex;align-items:center;gap:14px;font-family:'Oswald',sans-serif;font-weight:500}

/* hero */
.hero{left:0;top:0;width:1200px;height:650px;background:linear-gradient(180deg,#6f6a86 0%,#9a8ea2 30%,#56556a 60%,#3d4b33 85%,#2f3a28 100%)}
.brand{left:87px;top:30px;display:flex;align-items:center;gap:12px;font-family:'Oswald',sans-serif;font-size:30px;font-weight:500;color:var(--white)}
.brand-box{width:34px;height:34px;background:var(--blue)}
.top-phone{right:82px;top:26px;font-size:34px;color:var(--white)}
.hero-title{left:87px;top:204px;color:var(--white);font-weight:600;line-height:1.05}
.hero-title .l1{font-size:56px;display:block}
.hero-title .l2{font-size:34px;display:block;margin-top:4px}
.form{left:87px;top:322px;width:580px}
.field{position:absolute;height:48px;background:rgba(20,20,35,.55);color:#e8e8e8;font-size:15px;padding:14px 16px}
.field.select::after{content:"⌄";position:absolute;right:16px;top:8px}
.btn.hero-cta{left:87px;top:498px;width:216px;height:42px}

/* broker card */
.broker{left:29px;top:604px;width:1142px;height:334px;background:var(--white);box-shadow:0 4px 14px rgba(0,0,0,.18);text-align:center}
.broker h2{position:absolute;top:78px;width:100%;font-size:30px;font-weight:500}
.rule{width:62px;height:3px;background:var(--blue);margin:0 auto}
.broker .rule{position:absolute;top:127px;left:540px}
.broker p{position:absolute;top:150px;width:100%;font-size:15px;color:var(--muted)}
.broker .call{position:absolute;top:190px;width:100%;font-size:26px;text-transform:uppercase;color:var(--ink)}
.hl{color:var(--blue)}
.broker .phone{position:absolute;top:238px;left:490px;font-size:32px}

/* listings */
.listing{top:996px;width:324px;height:244px;overflow:hidden}
.listing .photo{width:100%;height:100%}
.listing .caption{position:absolute;left:0;bottom:0;width:100%;height:58px;background:rgba(2,85,163,.88);color:var(--white);font-size:14px;text-align:center;padding-top:8px;line-height:1.45}
.ribbon{position:absolute;right:0;top:0;width:58px;height:80px;background:var(--red);color:var(--white);text-align:center;font-family:'Oswald',sans-serif;clip-path:polygon(0 0,100% 0,100% 100%,50% 82%,0 100%)}
.ribbon small{display:block;font-size:10px;margin-top:12px}
.ribbon b{font-size:18px;font-weight:500}
.tagline{top:1276px;width:1200px;text-align:center;font-size:26px;text-transform:uppercase}

/* sell */
.sell-photo{left:446px;top:1380px;width:754px;height:453px;background:linear-gradient(135deg,#4a6b3a 0%,#6a8fa4 40%,#7d9cae 60%,#2f4a26 100%)}
.sell-panel{left:0;top:1426px;width:588px;height:364px;background:rgba(234,241,247,.96);padding:26px 0 0 90px}
.sell-panel h2{font-size:32px;font-weight:500}
.sell-panel .rule{margin:12px 0 12px}
.feature{display:flex;align-items:center;gap:20px;font-size:15px;color:#333;height:52px}
.feature svg{width:36px;height:36px;flex:none}
.btn.sell-cta{left:91px;top:1703px;width:216px;height:42px}

/* search */
.search{left:0;top:1912px;width:1200px;height:540px;background:linear-gradient(90deg,#f3f3f1 0%,#fbfbfa 60%,#eeeeec 100%)}
.laptop{left:88px;top:140px;width:560px;height:360px;background:linear-gradient(160deg,#3a2c22 0%,#7a5a3e 50%,#222 100%);border-radius:10px}
.vase-area{left:600px;top:40px;width:320px;height:440px;background:linear-gradient(180deg,#e4ece6 0%,#eef2ee 60%,#f3f4f2 100%)}
.search h2{left:729px;top:250px;font-size:30px;font-weight:500}
.search p{left:729px;top:314px;font-size:25px;line-height:1.35}

/* leasing */
.leasing h2{top:2524px;width:1200px;text-align:center;font-size:30px;font-weight:500}
.leasing .rule{position:absolute;left:569px;top:2578px}
.lease-item{top:2602px;width:300px;display:flex;gap:20px;font-size:15px;color:#444;line-height:1.55}
.lease-item svg{width:34px;height:34px;flex:none}
.btn.lease-cta{left:492px;top:2673px;width:218px;height:42px}

/* footer */
.footer{left:0;top:2793px;width:1200px;height:321px;background:var(--blue);color:var(--white)}
.footer h4{font-family:'Oswald',sans-serif;font-size:17px;font-weight:500;text-transform:uppercase}
.contact{left:87px;top:72px}
.contact li{list-style:none;display:flex;align-items:center;gap:22px;font-size:15px;margin-top:24px;line-height:1.5}
.dot{width:28px;height:28px;border-radius:50%;background:var(--white);flex:none}
.divider{top:76px;width:1px;height:190px;background:rgba(255,255,255,.35)}
.footer-brand{left:497px;top:76px;width:208px;height:124px;background:var(--white);display:flex;align-items:center;justify-content:center;gap:10px;font-family:'Oswald',sans-serif;font-size:24px;font-weight:500;color:var(--blue)}
.footer-brand span.sq{width:22px;height:22px;background:var(--blue)}
.copy{left:0;top:218px;width:1200px;text-align:center;font-size:14px}
.callus{left:885px;top:72px}
.callus .phone{margin-top:12px;font-size:32px}
.social{display:flex;gap:9px;margin-top:10px}
.social span{width:28px;height:28px;border-radius:50%;background:var(--white)}
</style>
</head>
<body>

<section class="hero abs" role="img" aria-label="Photo of a two-storey grey suburban house at dusk with lit windows and a green lawn"></section>
<div class="brand abs"><span class="brand-box"></span>Calmridge Realty</div>
<div class="phone top-phone abs">
  <svg width="36" height="36" viewBox="0 0 24 24" fill="#fff"><path d="M6.6 10.8a15.1 15.1 0 0 0 6.6 6.6l2.2-2.2c.3-.3.7-.4 1-.2 1.1.4 2.3.6 3.6.6.6 0 1 .4 1 1V20c0 .6-.4 1-1 1A17 17 0 0 1 3 4c0-.6.4-1 1-1h3.5c.6 0 1 .4 1 1 0 1.3.2 2.5.6 3.6.1.3 0 .7-.2 1z"/></svg>555-210-4870
</div>
<h1 class="hero-title abs display"><span class="l1">List for 1.5% Commission,</span><span class="l2">and receive top marketing from real estate pro!</span></h1>
<div class="form abs">
  <div class="field" style="left:0;top:0;width:290px">Name</div>
  <div class="field" style="left:300px;top:0;width:280px">Email</div>
  <div class="field" style="left:0;top:53px;width:290px">Phone</div>
  <div class="field select" style="left:300px;top:53px;width:280px">Buying Property</div>
  <div class="field" style="left:0;top:106px;width:580px">I'm interested in saving thousands by buying or selling with Calmridge Realty</div>
</div>
<div class="btn hero-cta">Contact us now</div>

<section class="broker abs">
  <h2 class="display">Marcus Delvane, Lic. Real Estate Broker</h2>
  <div class="rule"></div>
  <p>On average, our customers save $5,600 when they list with us... and they still receive top marketing and quality professional service!</p>
  <div class="call"><span class="hl">Call</span> us today and save <span class="hl">thousands $$$</span></div>
  <div class="phone">
    <svg width="40" height="40" viewBox="0 0 24 24" fill="#0255a3"><path d="M6.6 10.8a15.1 15.1 0 0 0 6.6 6.6l2.2-2.2c.3-.3.7-.4 1-.2 1.1.4 2.3.6 3.6.6.6 0 1 .4 1 1V20c0 .6-.4 1-1 1A17 17 0 0 1 3 4c0-.6.4-1 1-1h3.5c.6 0 1 .4 1 1 0 1.3.2 2.5.6 3.6.1.3 0 .7-.2 1z"/></svg>555-210-4870
  </div>
</section>

<article class="listing abs" style="left:87px">
  <div class="photo" role="img" aria-label="Photo of a white two-storey house with a blue roof among bare winter trees" style="background:linear-gradient(160deg,#9fb2c4,#e6e8ea 50%,#5a5046)"></div>
  <div class="ribbon"><small>SAVE</small><b>$4650</b></div>
  <div class="caption">4218 Willowmere Lane<br>Lakeport, FL 33901 - $310,000</div>
</article>
<article class="listing abs" style="left:438px">
  <div class="photo" role="img" aria-label="Photo of a white gabled house with a dark roof under a blue sky and green lawn" style="background:linear-gradient(180deg,#4d8fd6,#a9c9e8 45%,#d9dcd8 60%,#3f8a32)"></div>
  <div class="ribbon"><small>SAVE</small><b>$7485</b></div>
  <div class="caption">730 Vista Palma Boulevard, 202<br>Coral Bay, FL 33998 - $499,000</div>
</article>
<article class="listing abs" style="left:791px">
  <div class="photo" role="img" aria-label="Photo of a grey two-storey house with white trim and a front porch" style="background:linear-gradient(180deg,#b7c6d2,#8a9096 50%,#4c6a38)"></div>
  <div class="ribbon"><small>SAVE</small><b>$4650</b></div>
  <div class="caption">11520 Old Harrow Circle<br>Lakeport, FL 33903 - $310,000</div>
</article>
<p class="tagline abs"><span class="hl">30 day</span> listing service guaranteed. Save <span class="hl">thousands $$$</span> listing with us!</p>

<section class="sell-photo abs" role="img" aria-label="Photo of a blue Victorian house with red trim and a wraparound porch among trees"></section>
<section class="sell-panel abs">
  <h2 class="display">Sell with Calmridge &amp; Save $$$</h2>
  <div class="rule"></div>
  <div class="feature"><svg viewBox="0 0 24 24" fill="#0255a3"><path d="M4 7h3l2-2h6l2 2h3v12H4z"/><circle cx="12" cy="13" r="3.5" fill="#eaf1f7"/></svg>Professional Real Estate Photography</div>
  <div class="feature"><svg viewBox="0 0 24 24"><circle cx="12" cy="12" r="10" fill="#0255a3"/><path d="M8 15l3-3 2 2 3-4" stroke="#fff" stroke-width="2" fill="none"/></svg>Complimentary Comparative Market Analysis (CMA)</div>
  <div class="feature"><svg viewBox="0 0 24 24" fill="#0255a3"><circle cx="7" cy="6" r="3"/><path d="M2 20v-6a5 5 0 0 1 10 0v6z"/><rect x="13" y="9" width="9" height="11"/></svg>FREE Consultation with Real Estate Professional</div>
</section>
<div class="btn sell-cta">Contact us now</div>

<section class="search abs">
  <div class="vase-area abs" role="img" aria-label="Photo of a glass vase holding large green leaves on a white table"></div>
  <div class="laptop abs" role="img" aria-label="Photo of a laptop showing a virtual tour of a furnished living room"></div>
  <h2 class="abs display">Start your home search with us</h2>
  <p class="abs">1% Buyer Credit at Closing from<br><span class="hl">Calmridge Realty</span></p>
</section>

<section class="leasing">
  <h2 class="abs display">Leasing &amp; Property Management</h2>
  <div class="rule"></div>
  <div class="lease-item abs" style="left:87px"><svg viewBox="0 0 24 24" fill="none" stroke="#0255a3" stroke-width="2"><circle cx="12" cy="12" r="10"/><path d="M7 12l4 4 9-9"/></svg>We can manage your rental portfolio for you!</div>
  <div class="lease-item abs" style="left:457px"><svg viewBox="0 0 24 24" fill="none" stroke="#0255a3" stroke-width="2"><circle cx="12" cy="12" r="10"/><path d="M7 12l4 4 9-9"/></svg>Professional &amp; Experienced Property Managers</div>
  <div class="lease-item abs" style="left:829px"><svg viewBox="0 0 24 24" fill="none" stroke="#0255a3" stroke-width="2"><circle cx="12" cy="12" r="10"/><path d="M7 12l4 4 9-9"/></svg>Receive Top Dollar for your Rental Properties</div>
  <div class="btn lease-cta">Contact us now</div>
</section>

<footer class="footer abs">
  <div class="contact abs">
    <h4>Contact Info</h4>
    <ul>
      <li><span class="dot"></span>2400 Harbor View Blvd, Suite 310,<br>Coral Bay, FL 33999</li>
      <li><span class="dot"></span>contact@calmridge.us</li>
      <li><span class="dot"></span>www.calmridge.us</li>
    </ul>
  </div>
  <div class="divider abs" style="left:397px"></div>
  <div class="footer-brand abs"><span class="sq"></span>Calmridge Realty</div>
  <p class="copy abs">Copyright © 2018 &nbsp;|&nbsp; All Rights Reserved.</p>
  <div class="divider abs" style="left:805px"></div>
  <div class="callus abs">
    <h4>Call us now</h4>
    <div class="phone">
      <svg width="40" height="40" viewBox="0 0 24 24" fill="#fff"><path d="M6.6 10.8a15.1 15.1 0 0 0 6.6 6.6l2.2-2.2c.3-.3.7-.4 1-.2 1.1.4 2.3.6 3.6.6.6 0 1 .4 1 1V20c0 .6-.4 1-1 1A17 17 0 0 1 3 4c0-.6.4-1 1-1h3.5c.6 0 1 .4 1 1 0 1.3.2 2.5.6 3.6.1.3 0 .7-.2 1z"/></svg>555-210-4870
    </div>
    <h4 style="margin-top:22px">Social Links</h4>
    <div class="social"><span></span><span></span><span></span><span></span><span></span><span></span></div>
  </div>
</footer>

</body>
</html>
```